Business Card Design

We need a business card simular to the previous but including our logo our colours are royal blue, silver and black. we currently need cards for
Doug Pemberley Sales Manager 0400 295 617
doug@ridgelinegatesystems.com.au
Renee Blackwater 0415 832 190
renee@ridgelinegatesystems.com.au
Address 7 / 4 Marunga St Lonsdale
WEB www.ridgelinegatesystems.com.au
PH 84157203 Fax: 84157219
Updates
Good Morning all, I really don't like so much white. On the back I would like a list of all our products Security Doors & Screens, Built in Robes, Shower Screens, Blinds, Awnings, Roller Shutters & More Appointment Date & Time. Cheers Renee
Industry/Entity Type
Royal
Contact Information for Business Card
I really like the writing on our last business card from Cardmill.
Ridgeline Gate Systems , Factory Direct Prices, No Obligation Free Measure & Quote. List of Products Security Doors & Windows, Built in Robes, Indoor & Outdoor Blinds Inc Awnings & Velafolds, Shower Screens, Roller Shutters and More.
Font styles to use

```html
<!DOCTYPE html>
<html lang="en">
<head>
<meta charset="utf-8">
<title>Ridgeline Gate Systems – Business Card</title>
<link href="https://fonts.googleapis.com/css2?family=Open+Sans:wght@400;600;700&display=swap" rel="stylesheet">
<style>
  :root {
    --page: #e9e8e6;
    --card-black: #0b0d0f;
    --card-dark: #1a1d21;
    --royal: #1565b8;
    --royal-deep: #0c3f78;
    --silver: #d9dcdf;
    --silver-mid: #a9adb2;
    --text-light: #eceef0;
    --text-dim: #b8bcc1;
  }
  * { box-sizing: border-box; margin: 0; padding: 0; }
  html, body { width: 1200px; height: 800px; overflow: hidden; }
  body {
    background: var(--page);
    font-family: "Open Sans", Arial, sans-serif;
    display: flex; align-items: center; justify-content: center; gap: 40px;
  }
  .card {
    position: relative; width: 540px; height: 309px; overflow: hidden;
    background: linear-gradient(135deg, var(--card-dark), var(--card-black) 60%);
    color: var(--text-light);
    box-shadow: 0 10px 24px rgba(0,0,0,.25);
  }
  .texture {
    position: absolute; inset: 0;
    background: radial-gradient(ellipse at 40% 40%, #24282d 0%, #15181b 55%, #0b0d0f 100%);
  }
  .brand { position: absolute; display: flex; align-items: center; gap: 10px; }
  .brand-dot { width: 18px; height: 18px; border-radius: 50%; background: var(--silver); flex: none; }
  .brand-name {
    font-weight: 600; color: var(--silver); line-height: 1.05;
  }

  /* back */
  .card-back .brand { left: 40px; top: 70px; }
  .card-back .brand-name { font-size: 28px; width: 240px; }
  .products {
    position: absolute; left: 40px; right: 24px; top: 170px;
    font-size: 11.5px; line-height: 1.7; color: var(--text-light);
  }
  .appointment-strip {
    position: absolute; left: 0; right: 0; bottom: 0; height: 44px;
    background: linear-gradient(180deg, var(--silver), var(--silver-mid));
    display: flex; align-items: center; gap: 40px; padding: 0 40px;
    color: #2a2d31; font-size: 12px;
  }
  .appointment-strip span { flex: 1; border-bottom: 1px solid #2a2d31; padding-bottom: 2px; }

  /* front */
  .card-front .brand { right: 34px; top: 36px; }
  .card-front .brand-name { font-size: 26px; text-align: right; width: 220px; }
  .person { position: absolute; left: 34px; top: 118px; }
  .person-name { color: var(--royal); font-weight: 700; font-size: 14px; letter-spacing: .5px; text-transform: uppercase; }
  .person-role { font-size: 11px; color: var(--text-dim); margin-bottom: 10px; }
  .contact-line { display: flex; align-items: center; gap: 7px; font-size: 11.5px; margin-bottom: 5px; }
  .icon { width: 12px; height: 12px; flex: none; }
  .office { position: absolute; right: 40px; top: 188px; }
  .web-band {
    position: absolute; left: 0; right: 0; bottom: 0; height: 34px;
    background: linear-gradient(90deg, var(--royal-deep), var(--royal));
    display: flex; align-items: center; padding-left: 34px;
    font-size: 12.5px; letter-spacing: 2.5px; color: #fff;
  }
</style>
</head>
<body>

<section class="card card-back" aria-label="Card back">
  <div class="texture" role="img" aria-label="Dark hexagonal mesh background pattern"></div>
  <div class="brand">
    <span class="brand-dot"></span>
    <span class="brand-name">Ridgeline Gate Systems</span>
  </div>
  <p class="products">
    Security Doors &amp; Screens | Built in Robes | Shower Screens | Blinds<br>
    Awnings | Roller Shutters &amp; More Appointment Date &amp; Time. Cheers Renee
  </p>
  <div class="appointment-strip">Date:<span></span>Time:<span></span></div>
</section>

<section class="card card-front" aria-label="Card front">
  <div class="texture" role="img" aria-label="Dark hexagonal mesh background pattern"></div>
  <div class="brand">
    <span class="brand-dot"></span>
    <span class="brand-name">Ridgeline Gate Systems</span>
  </div>
  <div class="person">
    <p class="person-name">Doug Pemberley</p>
    <p class="person-role">Sales Manager</p>
    <p class="contact-line">
      <svg class="icon" viewBox="0 0 12 12"><rect width="12" height="12" rx="2" fill="#1565b8"/><rect x="4" y="2.5" width="4" height="7" rx="1" fill="none" stroke="#fff" stroke-width="1"/></svg>
      0400 295 617
    </p>
    <p class="contact-line">
      <svg class="icon" viewBox="0 0 12 12"><rect width="12" height="12" rx="2" fill="#1565b8"/><rect x="2.5" y="3.5" width="7" height="5" fill="none" stroke="#fff" stroke-width="1"/><path d="M2.5 3.5 6 6.5 9.5 3.5" fill="none" stroke="#fff" stroke-width="1"/></svg>
      doug@ridgelinegatesystems.com.au
    </p>
  </div>
  <div class="office">
    <p class="contact-line">
      <svg class="icon" viewBox="0 0 12 12"><rect width="12" height="12" rx="2" fill="#1565b8"/><path d="M6 2.5a2.3 2.3 0 0 1 2.3 2.3C8.3 6.6 6 9.5 6 9.5S3.7 6.6 3.7 4.8A2.3 2.3 0 0 1 6 2.5z" fill="#fff"/></svg>
      7/4 Marunga St Lonsdale
    </p>
    <p class="contact-line">
      <svg class="icon" viewBox="0 0 12 12"><rect width="12" height="12" rx="2" fill="#1565b8"/><path d="M3.5 3c.5-.5 1-.5 1.4 0l.6.9c.3.4.2.8-.1 1.1-.3.3.9 1.6 1.3 1.4.3-.3.7-.4 1.1-.1l.9.6c.5.4.5.9 0 1.4-1.4 1.3-6.5-3.6-5.2-5.3z" fill="#fff"/></svg>
      84157203
    </p>
    <p class="contact-line">
      <svg class="icon" viewBox="0 0 12 12"><rect width="12" height="12" rx="2" fill="#1565b8"/><rect x="3" y="5" width="6" height="4" fill="#fff"/><rect x="4" y="2.5" width="4" height="2.5" fill="none" stroke="#fff" stroke-width="1"/></svg>
      84157219
    </p>
  </div>
  <div class="web-band">www.ridgelinegatesystems.com.au</div>
</section>

</body>
</html>
```